Update existing icons for an admin interface to look more professional high end

Please see attached 4 files.
One from a competitor system which looks more high end and our icon files and how they look in the interface.
We need to suit to high end network administrators and need a more professional high end look. They need be in the same blueish color theme.

```html
<!DOCTYPE html>
<html lang="en">
<head>
<meta charset="utf-8">
<title>Admin Navigation Menus</title>
<link rel="stylesheet" href="https://fonts.googleapis.com/css2?family=Arimo:wght@400;700&display=swap">
<style>
  :root {
    --bg-center: #efefef;
    --bg-edge: #d3d3d3;
    --row-top: #2b414c;
    --row-bottom: #1b2b33;
    --row-line: #0e181d;
    --row-highlight: rgba(255,255,255,0.07);
    --active-top: #1d7898;
    --active-bottom: #0c4256;
    --text: #e4edf1;
    --icon: #1fc3f2;
    --badge-bg: #0b161b;
    --badge-border: #9fb0b8;
    --panel-white: #ffffff;
  }
  * { box-sizing: border-box; margin: 0; padding: 0; }
  html, body { width: 1200px; height: 916px; overflow: hidden; }
  body {
    position: relative;
    background: radial-gradient(ellipse at 50% 60%, var(--bg-center) 0%, #e3e3e3 45%, var(--bg-edge) 100%);
    font-family: "Arimo", Arial, sans-serif;
  }
  .nav-panel {
    position: absolute;
    top: 93px;
    background: var(--panel-white);
    box-shadow: 0 1px 4px rgba(0,0,0,0.35);
  }
  .nav-panel--scanner { left: 183px; width: 365px; height: 463px; padding-right: 3px; border-right: 1px solid #9a9a9a; }
  .nav-panel--protector { left: 661px; width: 354px; height: 747px; }
  .nav-list { list-style: none; }
  .nav-item {
    position: relative;
    height: 33.65px;
    display: flex;
    align-items: center;
    background: linear-gradient(var(--row-top), var(--row-bottom));
    border-bottom: 1px solid var(--row-line);
    box-shadow: inset 0 1px 0 var(--row-highlight);
    color: var(--text);
    font-size: 11.5px;
    letter-spacing: 0.1px;
  }
  .nav-item--active {
    background: linear-gradient(var(--active-top), var(--active-bottom));
    font-weight: 700;
    color: #ffffff;
  }
  .nav-item--active::after {
    content: "";
    position: absolute;
    right: 0;
    top: 50%;
    margin-top: -7px;
    border: 7px solid transparent;
    border-right-color: var(--panel-white);
    border-left-width: 0;
  }
  .nav-icon {
    width: 19px;
    height: 19px;
    margin-left: 12px;
    margin-right: 4px;
    flex: none;
    fill: var(--icon);
    stroke: var(--icon);
  }
  .nav-label { flex: 1; }
  .nav-badge {
    margin-right: 9px;
    min-width: 21px;
    height: 18px;
    padding: 0 5px;
    display: flex;
    align-items: center;
    justify-content: center;
    background: var(--badge-bg);
    border: 1px solid var(--badge-border);
    border-radius: 2px;
    color: #ffffff;
    font-size: 10.5px;
    font-weight: 700;
    box-shadow: 0 0 2px rgba(0,0,0,0.6);
  }
  .icon-defs { position: absolute; width: 0; height: 0; }
</style>
</head>
<body>

<svg class="icon-defs" aria-hidden="true">
  <defs>
    <symbol id="i-home" viewBox="0 0 20 20"><rect x="2" y="3" width="16" height="11" rx="1" stroke="none"/><rect x="4" y="5" width="12" height="7" fill="#1b2b33" stroke="none"/><rect x="8" y="14" width="4" height="3" stroke="none"/><rect x="5" y="17" width="10" height="1.6" stroke="none"/></symbol>
    <symbol id="i-scanner" viewBox="0 0 20 20"><path d="M4 4 L4 16 M4 4 L16 16 M16 4 L16 16" fill="none" stroke-width="2.4"/><circle cx="4" cy="4" r="3" stroke="none"/><circle cx="16" cy="16" r="3" stroke="none"/><circle cx="16" cy="4" r="2.4" stroke="none"/><circle cx="4" cy="16" r="2.4" stroke="none"/></symbol>
    <symbol id="i-clock" viewBox="0 0 20 20"><circle cx="10" cy="10" r="8.5" stroke="none"/><path d="M10 4 V10 H5" fill="none" stroke="#1b2b33" stroke-width="2"/></symbol>
    <symbol id="i-chart" viewBox="0 0 20 20"><path d="M2 2 V17 H18" fill="none" stroke-width="1.8"/><path d="M4 14 L8 8 L11 11 L17 4" fill="none" stroke-width="2"/></symbol>
    <symbol id="i-ticket" viewBox="0 0 20 20"><path d="M3 13 L13 3 L17 7 L7 17 Z" stroke="none"/><path d="M6 12 L12 6" stroke="#1b2b33" stroke-width="1.2" stroke-dasharray="1.5 1.5"/></symbol>
    <symbol id="i-wifi" viewBox="0 0 20 20"><path d="M2 8 A11 11 0 0 1 18 8 M4.5 11 A7.5 7.5 0 0 1 15.5 11 M7 14 A4 4 0 0 1 13 14" fill="none" stroke-width="2.2"/><circle cx="10" cy="17" r="1.6" stroke="none"/></symbol>
    <symbol id="i-user" viewBox="0 0 20 20"><circle cx="10" cy="6" r="4" stroke="none"/><path d="M2 19 C2 12 18 12 18 19 Z" stroke="none"/></symbol>
    <symbol id="i-dist" viewBox="0 0 20 20"><rect x="1" y="2" width="18" height="13" rx="1" fill="none" stroke-width="1.8"/><path d="M4 8.5 H16 M4 8.5 L7 6 M4 8.5 L7 11 M16 8.5 L13 6 M16 8.5 L13 11" fill="none" stroke-width="1.8"/><rect x="7" y="16" width="6" height="2" stroke="none"/></symbol>
    <symbol id="i-gear" viewBox="0 0 20 20"><circle cx="10" cy="10" r="6" stroke-width="0"/><path d="M10 1 V19 M1 10 H19 M3.6 3.6 L16.4 16.4 M16.4 3.6 L3.6 16.4" stroke-width="3"/><circle cx="10" cy="10" r="2.5" fill="#1b2b33" stroke="none"/></symbol>
    <symbol id="i-network" viewBox="0 0 20 20"><rect x="1" y="2" width="7" height="5" stroke="none"/><rect x="12" y="2" width="7" height="5" stroke="none"/><rect x="7" y="13" width="6" height="5" stroke="none"/><path d="M4.5 7 V10 H15.5 V7 M10 10 V13" fill="none" stroke-width="1.6"/></symbol>
    <symbol id="i-update" viewBox="0 0 20 20"><path d="M16 7 A7 7 0 0 0 3.5 8 M4 13 A7 7 0 0 0 16.5 12" fill="none" stroke-width="2.6"/><path d="M13 6 L18 8 L18 2 Z M7 14 L2 12 L2 18 Z" stroke="none"/></symbol>
    <symbol id="i-support" viewBox="0 0 20 20"><circle cx="10" cy="10" r="7" fill="none" stroke-width="4"/><path d="M4 4 L7.5 7.5 M16 4 L12.5 7.5 M4 16 L7.5 12.5 M16 16 L12.5 12.5" stroke="#1b2b33" stroke-width="2"/></symbol>
    <symbol id="i-mail" viewBox="0 0 20 20"><rect x="1.5" y="4" width="17" height="12" fill="none" stroke-width="1.8"/><path d="M1.5 4 L10 11 L18.5 4" fill="none" stroke-width="1.8"/></symbol>
    <symbol id="i-spam" viewBox="0 0 20 20"><path d="M1.5 2 H17.5 V9 M1.5 2 V14 H10 M1.5 2 L9.5 8.5 L17.5 2" fill="none" stroke-width="1.6"/><circle cx="14.5" cy="14.5" r="4" fill="none" stroke-width="1.5"/><path d="M11.7 17.3 L17.3 11.7" stroke-width="1.5"/></symbol>
    <symbol id="i-archive" viewBox="0 0 20 20"><rect x="2" y="5" width="16" height="13" fill="none" stroke-width="1.8"/><path d="M5 5 V2 H15 V5 M2 9 L10 13 L18 9" fill="none" stroke-width="1.6"/></symbol>
    <symbol id="i-shield" viewBox="0 0 20 20"><path d="M10 1 L18 4 V9 C18 14 14 17.5 10 19 C6 17.5 2 14 2 9 V4 Z" stroke="none"/><path d="M10 3 V17 C13 15.5 16 13 16 9 V5.3 Z" fill="#1b2b33" stroke="none"/></symbol>
    <symbol id="i-firewall" viewBox="0 0 20 20"><path d="M1 2 H6 V5 H1 Z M7 2 H12 V5 H7 Z M1 7 H4 V10 H1 Z M5 7 H10 V10 H5 Z M1 12 H6 V15 H1 Z M1 17 H10 V19 H1 Z" stroke="none"/><path d="M14 8 C17 11 18 13 18 15 A3.5 3.5 0 0 1 11 15 C11 12 14 11 14 8 Z" stroke="none"/></symbol>
    <symbol id="i-globe" viewBox="0 0 20 20"><circle cx="10" cy="10" r="8.5" fill="none" stroke-width="1.8"/><ellipse cx="10" cy="10" rx="3.5" ry="8.5" fill="none" stroke-width="1.5"/><path d="M1.5 10 H18.5 M3 5.5 H17 M3 14.5 H17" fill="none" stroke-width="1.4"/></symbol>
    <symbol id="i-shaper" viewBox="0 0 20 20"><rect x="1" y="1" width="18" height="18" rx="4" stroke="none"/><path d="M2 13 L6 13 L8 5 L11 16 L13 9 L18 13" fill="none" stroke="#1b2b33" stroke-width="1.6"/></symbol>
    <symbol id="i-mask" viewBox="0 0 20 20"><path d="M1 8 C4 6 7 7 10 9 C13 7 16 6 19 8 C19 12 16 14 13 12 L10 11 L7 12 C4 14 1 12 1 8 Z" stroke="none"/><circle cx="6" cy="9.5" r="1.5" fill="#1b2b33" stroke="none"/><circle cx="14" cy="9.5" r="1.5" fill="#1b2b33" stroke="none"/></symbol>
    <symbol id="i-funnel" viewBox="0 0 20 20"><path d="M1 2 H19 L12 10 V19 L8 16 V10 Z" stroke="none"/></symbol>
    <symbol id="i-gauge" viewBox="0 0 20 20"><path d="M2 15 A8 8 0 1 1 18 15 Z" fill="none" stroke-width="2"/><path d="M10 14 L14 7" stroke-width="2"/><circle cx="10" cy="14" r="1.8" stroke="none"/></symbol>
    <symbol id="i-247" viewBox="0 0 20 20"><circle cx="10" cy="10" r="9" stroke="none"/><circle cx="10" cy="10" r="7" fill="#125a72" stroke="none"/><text x="10" y="12.6" text-anchor="middle" font-family="Arimo, Arial, sans-serif" font-size="7" font-weight="700" fill="#ffffff" stroke="none">24/7</text></symbol>
  </defs>
</svg>

<nav class="nav-panel nav-panel--scanner" aria-label="Scanner navigation">
  <ul class="nav-list">
    <li class="nav-item"><svg class="nav-icon"><use href="#i-home"/></svg><span class="nav-label">Home</span></li>
    <li class="nav-item"><svg class="nav-icon"><use href="#i-scanner"/></svg><span class="nav-label">Vulnerability Scanner</span><span class="nav-badge">10</span></li>
    <li class="nav-item"><svg class="nav-icon"><use href="#i-clock"/></svg><span class="nav-label">Schedule</span><span class="nav-badge">2</span></li>
    <li class="nav-item"><svg class="nav-icon"><use href="#i-chart"/></svg><span class="nav-label">Statistics</span><span class="nav-badge">2</span></li>
    <li class="nav-item"><svg class="nav-icon"><use href="#i-ticket"/></svg><span class="nav-label">Tickets</span><span class="nav-badge">3</span></li>
    <li class="nav-item"><svg class="nav-icon"><use href="#i-wifi"/></svg><span class="nav-label">WiFi Pen Test</span><span class="nav-badge">15</span></li>
    <li class="nav-item"><svg class="nav-icon"><use href="#i-user"/></svg><span class="nav-label">Cloud Users</span><span class="nav-badge">5</span></li>
    <li class="nav-item nav-item--active"><svg class="nav-icon"><use href="#i-dist"/></svg><span class="nav-label">Scan Distribution</span></li>
    <li class="nav-item"><svg class="nav-icon"><use href="#i-gear"/></svg><span class="nav-label">System</span><span class="nav-badge">19</span></li>
    <li class="nav-item"><svg class="nav-icon"><use href="#i-network"/></svg><span class="nav-label">Network Setup</span><span class="nav-badge">4</span></li>
    <li class="nav-item"><svg class="nav-icon"><use href="#i-update"/></svg><span class="nav-label">Update</span><span class="nav-badge">4</span></li>
    <li class="nav-item"><svg class="nav-icon"><use href="#i-support"/></svg><span class="nav-label">Support</span><span class="nav-badge">19</span></li>
  </ul>
</nav>

<nav class="nav-panel nav-panel--protector" aria-label="Protector navigation">
  <ul class="nav-list">
    <li class="nav-item"><svg class="nav-icon"><use href="#i-home"/></svg><span class="nav-label">Home</span></li>
    <li class="nav-item"><svg class="nav-icon"><use href="#i-chart"/></svg><span class="nav-label">Statistics &amp; Logs</span><span class="nav-badge">7</span></li>
    <li class="nav-item"><svg class="nav-icon"><use href="#i-spam"/></svg><span class="nav-label">Anti Spam</span><span class="nav-badge">8</span></li>
    <li class="nav-item"><svg class="nav-icon"><use href="#i-archive"/></svg><span class="nav-label">Mail Archiver</span><span class="nav-badge">4</span></li>
    <li class="nav-item"><svg class="nav-icon"><use href="#i-shield"/></svg><span class="nav-label">Anti Virus</span></li>
    <li class="nav-item"><svg class="nav-icon"><use href="#i-mail"/></svg><span class="nav-label">E-Mail</span><span class="nav-badge">4</span></li>
    <li class="nav-item"><svg class="nav-icon"><use href="#i-firewall"/></svg><span class="nav-label">Firewall</span><span class="nav-badge">11</span></li>
    <li class="nav-item"><svg class="nav-icon"><use href="#i-dist"/></svg><span class="nav-label">VPN</span><span class="nav-badge">5</span></li>
    <li class="nav-item"><svg class="nav-icon"><use href="#i-globe"/></svg><span class="nav-label">Web Filter</span><span class="nav-badge">4</span></li>
    <li class="nav-item"><svg class="nav-icon"><use href="#i-shaper"/></svg><span class="nav-label">Traffic Shaper</span></li>
    <li class="nav-item"><svg class="nav-icon"><use href="#i-mask"/></svg><span class="nav-label">IPS - Malware</span><span class="nav-badge">2</span></li>
    <li class="nav-item"><svg class="nav-icon"><use href="#i-wifi"/></svg><span class="nav-label">WiFi Defender</span></li>
    <li class="nav-item"><svg class="nav-icon"><use href="#i-funnel"/></svg><span class="nav-label">Content Filter</span></li>
    <li class="nav-item"><svg class="nav-icon"><use href="#i-scanner"/></svg><span class="nav-label">Vulnerability Scanner</span><span class="nav-badge">2</span></li>
    <li class="nav-item"><svg class="nav-icon"><use href="#i-gauge"/></svg><span class="nav-label">Alert Center</span><span class="nav-badge">7</span></li>
    <li class="nav-item"><svg class="nav-icon"><use href="#i-user"/></svg><span class="nav-label">Protector Users</span></li>
    <li class="nav-item"><svg class="nav-icon"><use href="#i-gear"/></svg><span class="nav-label">System</span><span class="nav-badge">13</span></li>
    <li class="nav-item"><svg class="nav-icon"><use href="#i-network"/></svg><span class="nav-label">Network Setup</span><span class="nav-badge">8</span></li>
    <li class="nav-item nav-item--active"><svg class="nav-icon"><use href="#i-247"/></svg><span class="nav-label">High Availability</span></li>
    <li class="nav-item"><svg class="nav-icon"><use href="#i-update"/></svg><span class="nav-label">Update</span><span class="nav-badge">3</span></li>
    <li class="nav-item"><svg class="nav-icon"><use href="#i-support"/></svg><span class="nav-label">Support</span><span class="nav-badge">13</span></li>
  </ul>
</nav>

</body>
</html>
```